I am looking for a stand-out cover that sings out to new parents. The category is very pastel with limited compelling covers that would make me want to buy a book. This book will be used often in the first 12 months of baby's life - so must be strong enough to sit on the bedside table or on the coffee table to inspire reading. It will be a popular gift - so needs to look credible, "pick-up-able" and loveable.

The Book Title is - The Cradle Compass to Infancy's Opening Seasons: Grounded, Research-Led Methods on Rest, Nourishment, Protection plus Growing Assurance
The Size is - 8.5 x 11 in
Book description to be provided to final design for inclusion
Some examples of book covers in this category attached. Thanks

```html
<!DOCTYPE html>
<html lang="en">
<head>
<meta charset="utf-8">
<title>The Cradle Compass to Infancy's Opening Seasons</title>
<link href="https://fonts.googleapis.com/css2?family=Cormorant+SC:wght@500;600&family=EB+Garamond:ital,wght@0,400;0,500;1,400&display=swap" rel="stylesheet">
<style>
  :root {
    --page: #ffffff;
    --paper: #f8e6df;
    --paper-light: #fbefe9;
    --sage: #9fb2a6;
    --sage-deep: #7f988c;
    --gold: #e8cf96;
    --blush: #ecc3b2;
    --skin: #f0c8ae;
    --ink-green: #3f5448;
    --terracotta: #b9604b;
    --rule-gold: #b08f5c;
  }
  * { margin: 0; padding: 0; box-sizing: border-box; }
  html, body {
    width: 1200px; height: 1200px; overflow: hidden;
    background: var(--page);
  }
  .cover {
    position: absolute;
    left: 230px; top: 44px;
    width: 740px; height: 1112px;
    overflow: hidden;
    background: linear-gradient(180deg, var(--paper-light), var(--paper));
  }
  .art-haze {
    position: absolute; inset: 0;
  }
  .art-sleep {
    position: absolute;
    left: 30px; top: 96px; width: 560px; height: 190px;
    border-radius: 50% 50% 46% 54% / 60% 55% 45% 40%;
    background:
      radial-gradient(ellipse 22% 34% at 44% 40%, var(--skin) 0%, rgba(240,200,174,.85) 55%, rgba(240,200,174,0) 100%),
      radial-gradient(ellipse 20% 30% at 22% 58%, #f3e4dc 0%, rgba(243,228,220,0) 100%),
      radial-gradient(ellipse 42% 46% at 72% 48%, #c4d3c9 0%, rgba(196,211,201,0) 100%),
      linear-gradient(180deg, rgba(238,220,210,.9), rgba(214,222,212,.95));
    filter: blur(2px);
  }
  .art-items {
    position: absolute; left: 0; top: 0; width: 740px; height: 1112px;
  }
  .title-block {
    position: absolute; left: 0; right: 0; top: 324px;
    text-align: center;
  }
  .kicker {
    font-family: "Cormorant SC", serif;
    font-weight: 600;
    font-size: 34px;
    letter-spacing: 3px;
    color: var(--terracotta);
    line-height: 40px;
  }
  .main-title {
    font-family: "Cormorant SC", serif;
    font-weight: 600;
    font-size: 106px;
    line-height: 86px;
    color: var(--ink-green);
    margin-top: 4px;
  }
  .series-line {
    display: flex; align-items: center; justify-content: center; gap: 14px;
    margin-top: 14px;
    font-family: "EB Garamond", serif;
    font-weight: 500;
    font-size: 30px;
    color: var(--ink-green);
  }
  .series-line .small { font-style: italic; font-size: 20px; margin-right: -6px; }
  .series-line .rule { width: 32px; height: 1px; background: var(--rule-gold); opacity: .7; }
  .divider { display: block; margin: 22px auto 0; }
  .subtitle {
    margin-top: 16px;
    font-family: "EB Garamond", serif;
    font-size: 20px;
    line-height: 31px;
    color: var(--terracotta);
  }
</style>
</head>
<body>
  <main class="cover">
    <svg class="art-haze" viewBox="0 0 740 1112" aria-hidden="true">
      <defs>
        <radialGradient id="topHaze" cx=".25" cy=".22" r=".6">
          <stop offset="0" stop-color="#9fb2a6" stop-opacity=".85"/>
          <stop offset=".6" stop-color="#b9c6b8" stop-opacity=".45"/>
          <stop offset="1" stop-color="#f8e6df" stop-opacity="0"/>
        </radialGradient>
      </defs>
      <path d="M0 0 H560 C640 60 660 160 600 240 C520 320 380 300 280 380 C200 440 120 420 0 460 Z" fill="url(#topHaze)"/>
    </svg>

    <div class="art-sleep" role="img" aria-label="Watercolour of a sleeping baby tucked under a blanket beside a plush bunny"></div>

    <svg class="art-items" viewBox="0 0 740 1112" role="img" aria-label="Watercolour swirl of baby bottles, alarm clock, nappy, bib, pacifier and hearts">
      <defs>
        <linearGradient id="swash" x1="1" y1="0" x2="0" y2="1">
          <stop offset="0" stop-color="#ecc3b2" stop-opacity=".7"/>
          <stop offset=".3" stop-color="#e8cf96" stop-opacity=".9"/>
          <stop offset=".6" stop-color="#9fb2a6" stop-opacity=".9"/>
          <stop offset="1" stop-color="#e6c1ac" stop-opacity=".85"/>
        </linearGradient>
        <radialGradient id="glow" cx=".45" cy=".55" r=".5">
          <stop offset="0" stop-color="#f5e2b4" stop-opacity=".95"/>
          <stop offset="1" stop-color="#f5e2b4" stop-opacity="0"/>
        </radialGradient>
        <linearGradient id="mist" x1="0" y1="0" x2="1" y2="1">
          <stop offset="0" stop-color="#ffffff" stop-opacity="0"/>
          <stop offset="1" stop-color="#ffffff" stop-opacity=".5"/>
        </linearGradient>
      </defs>
      <path d="M740 440 C700 540 610 620 520 700 C410 800 250 870 170 970 C130 1020 130 1080 150 1112 L740 1112 Z" fill="url(#swash)"/>
      <ellipse cx="470" cy="830" rx="230" ry="120" fill="url(#glow)"/>
      <path d="M740 900 C640 960 560 1020 470 1112 L740 1112 Z" fill="#8fa598" opacity=".45"/>
      <path d="M200 1010 C320 950 470 930 620 880" stroke="url(#mist)" stroke-width="2" fill="none"/>
      <path d="M180 1060 C320 1000 500 990 700 930" stroke="#ffffff" stroke-opacity=".45" stroke-width="1.5" fill="none"/>
      <path d="M560 720 C620 680 680 640 730 590" stroke="#ffffff" stroke-opacity=".5" stroke-width="1.5" fill="none"/>
    </svg>

    <header class="title-block">
      <p class="kicker">The</p>
      <h1 class="main-title">Cradle<br>Compass</h1>
      <p class="series-line"><span class="rule"></span><span class="small">to</span> Infancy’s Opening Seasons<span class="rule"></span></p>
      <svg class="divider" width="396" height="10" viewBox="0 0 396 10" aria-hidden="true">
        <line x1="0" y1="5" x2="176" y2="5" stroke="#b08f5c" stroke-width="1"/>
        <line x1="220" y1="5" x2="396" y2="5" stroke="#b08f5c" stroke-width="1"/>
        <ellipse cx="198" cy="5" rx="14" ry="3" fill="#b08f5c"/>
      </svg>
      <p class="subtitle">Grounded, Research-Led Methods on Rest,<br>Nourishment, Protection plus Growing Assurance</p>
    </header>
  </main>
</body>
</html>
```